Home Services Website Design and Revisions

We have started to create a website but I would like to get some ideas and a quote on how to create a more professional website then what we have created thus far.

http://brinkhavenhomecare.example/

Pages I would need on the site

Home page - company summary and brand promise
who we are
what we do - services offered
our promise to quality and client experience
client experiences - testimonials and pictures
Promotions
Career opportunities - Join The team
Updates

Target Market(s)

Homeowners in the DFW region

Industry/Entity Type

Home Improvement

Number of Pages Required

5+ page

Font styles to use
Sans Serif

Requirements
Must have
• Home page - company summary and brand promise
• who we are
• what we do - services offered
• our promise to quality and client experience
• client experiences - testimonials and pictures
• Promotions
• Career opportunities - Join The team
• logo
• pictures
• links to social media sites
• A very impactful home page
• With a image of home and family.
• a beautiful home, yard and pictures of a loving family smiling and enjoying their home.
Nice to have
• Pictures with people to create emotion
• we don't work on houses
• we work on homes with families that trust us to provide quality services in a timely manner
• Families that trust us as their partner when they need work at their home with their family
Should not have
• low quality images or images just of homes

```html
<!DOCTYPE html>
<html lang="en">
<head>
<meta charset="utf-8">
<title>Brinkhaven Painting and Home Services Experts</title>
<link href="https://fonts.googleapis.com/css2?family=Open+Sans:wght@400;600;700&family=Raleway:wght@400;500;600&display=swap" rel="stylesheet">
<style>
:root{
  --green:#5fb513;
  --green-dark:#4e9a0c;
  --ink:#333333;
  --body:#666666;
  --muted:#8a8a8a;
  --grey-btn:#8c8c8c;
  --panel:#f6f6f6;
  --footer:#f3f3f3;
  --white:#ffffff;
  --star:#f2b01e;
  --star-off:#d6d6d6;
}
*{box-sizing:border-box;margin:0;padding:0}
html,body{width:1200px;height:2362px;overflow:hidden}
body{position:relative;background:var(--white);font-family:"Open Sans",Arial,sans-serif;color:var(--body)}
.abs{position:absolute}
h1,h2,h3,h4{font-family:"Raleway",Arial,sans-serif;font-weight:500;color:var(--ink)}
.btn{position:absolute;display:flex;align-items:center;justify-content:center;border-radius:20px;font-size:12px;font-weight:600;color:var(--white);background:var(--green);height:36px}
.btn.grey{background:var(--grey-btn)}
.btn.light{background:var(--white);color:var(--ink)}
p{font-size:12.5px;line-height:22px}

/* header */
.site-header{position:absolute;left:0;top:0;width:1200px;height:47px;background:var(--white)}
.brand{position:absolute;left:88px;top:7px;display:flex;align-items:center;gap:8px}
.brand-mark{width:30px;height:30px;background:var(--green);border-radius:3px}
.brand-name{font-family:"Open Sans",Arial,sans-serif;font-weight:700;font-size:11px;line-height:13px;color:var(--ink);text-transform:uppercase}
.brand-name span{display:block;font-weight:700;font-size:7px;letter-spacing:.2px}
.main-nav{position:absolute;top:0;left:650px;display:flex;gap:24px;height:47px;align-items:center}
.main-nav a{font-size:12.5px;color:var(--ink);text-decoration:none;height:47px;line-height:47px}
.main-nav a.active{color:var(--green);border-bottom:2px solid var(--green)}

/* hero */
.hero{position:absolute;left:0;top:47px;width:1200px;height:460px}
.hero-photo{position:absolute;inset:0;background:linear-gradient(90deg,#e8cbb6 0%,#d9e6ec 38%,#eaf4f8 60%,#f6fbfd 100%)}
.hero-copy{position:absolute;left:792px;top:116px;width:330px}
.hero-copy h1{font-size:28px;color:var(--ink);margin-bottom:10px}
.hero-copy p{font-size:12px;line-height:22px}
.hero .btn{left:792px;top:236px;width:108px}
.slide-arrow{position:absolute;top:208px;width:44px;height:44px;border-radius:50%;display:flex;align-items:center;justify-content:center}
.slide-arrow.prev{left:17px;background:#333}
.slide-arrow.next{left:1137px;background:var(--green)}
.slide-dot{position:absolute;left:594px;top:432px;width:10px;height:10px;border-radius:50%;background:var(--green)}

/* who we are */
.who{position:absolute;left:0;top:507px;width:1200px;height:323px}
.who h2{position:absolute;left:107px;width:536px;top:30px;text-align:right;font-size:22px}
.who p{position:absolute;left:107px;width:536px;top:70px;text-align:center;font-size:11.5px;line-height:22px}
.who .btn{left:537px;top:216px;width:108px}
.collage{position:absolute;left:665px;top:441px;width:430px;height:340px}

/* what we do */
.services{position:absolute;left:0;top:830px;width:1200px;height:367px;background:var(--panel)}
.services h2{position:absolute;left:0;width:1200px;top:27px;text-align:center;font-size:22px}
.service{position:absolute;top:64px;width:320px;text-align:center}
.service svg{display:block;margin:0 auto}
.service h3{font-size:16px;margin-top:20px;font-family:"Open Sans",Arial,sans-serif;font-weight:400}
.service p{font-size:11.5px;line-height:22px;margin-top:6px;padding:0 10px}
.service .btn{position:relative;margin:12px auto 0;width:110px}

/* promise */
.promise{position:absolute;left:0;top:1197px;width:1200px;height:192px;background:linear-gradient(90deg,#63bd16,#58ae10 50%,#66c01a)}
.promise h2{position:absolute;left:0;width:1200px;top:28px;text-align:center;color:var(--white);font-size:22px}
.promise p{position:absolute;left:260px;width:680px;top:62px;text-align:center;color:var(--white);font-size:11.5px;line-height:23px}
.promise .btn{left:539px;top:126px;width:110px}

/* testimonials */
.clients{position:absolute;left:0;top:1389px;width:1200px;height:281px}
.clients h2{position:absolute;left:0;width:1200px;top:22px;text-align:center;font-size:22px}
.testimonial{position:absolute;top:79px;width:520px;height:170px}
.t-frame{position:absolute;left:0;top:0;width:173px;height:167px;border:3px solid var(--green);border-left-width:10px;border-top-width:10px}
.t-photo{position:absolute;left:8px;top:8px;width:147px;height:149px;background:linear-gradient(160deg,#c9c4bd,#8d8a86)}
.t-quote{position:absolute;left:190px;top:18px;font-family:Georgia,serif;font-size:44px;line-height:30px;color:#e1e1e1}
.t-name{position:absolute;left:222px;top:26px;font-size:14px;color:var(--green);font-weight:400}
.t-text{position:absolute;left:222px;top:56px;width:300px;font-size:11.5px;line-height:22px}
.stars{position:absolute;left:222px;top:131px;display:flex;gap:3px}
.pager{position:absolute;left:46px;top:1517px}
.pager i{display:block;width:8px;height:8px;border-radius:50%;background:#d8d8d8;margin-bottom:6px}
.pager i.on{background:var(--green)}

/* promotions */
.promos{position:absolute;left:0;top:1670px;width:1200px;height:231px;background:var(--panel)}
.promos h2{position:absolute;left:0;width:1200px;top:18px;text-align:center;font-size:22px}
.promo{position:absolute;top:50px;width:188px;height:152px}
.promo svg{position:absolute;left:0;top:0}
.promo h3{position:absolute;left:0;width:188px;top:65px;text-align:center;font-size:17px;font-family:"Open Sans",Arial,sans-serif;font-weight:400;color:var(--ink)}
.promo p{position:absolute;left:30px;width:128px;top:90px;text-align:center;font-size:11.5px;line-height:22px}

/* careers */
.careers{position:absolute;left:0;top:1901px;width:1200px;height:238px}
.careers-photo{position:absolute;left:88px;top:31px;width:214px;height:171px;background:linear-gradient(135deg,#f1d9bd,#c9926a 55%,#a5c4d9)}
.careers h2{position:absolute;left:329px;top:58px;font-size:22px}
.careers h2 em{font-style:normal;color:var(--green);font-size:17px;font-family:"Open Sans",Arial,sans-serif;margin-left:8px}
.careers p{position:absolute;left:333px;top:92px;width:740px;font-size:11.5px;line-height:22px}
.careers .btn{left:324px;top:146px;width:117px}

/* footer */
.site-footer{position:absolute;left:0;top:2139px;width:1200px;height:189px;background:var(--footer)}
.f-col{position:absolute;top:18px}
.f-col h4{font-size:15px;margin-bottom:10px}
.f-col p,.f-col li{font-size:11.5px;line-height:20px;color:var(--body);list-style:none}
.social{display:flex;gap:8px;margin-top:12px}
.social span{width:30px;height:30px;border-radius:50%;background:var(--green)}
.contact-row{display:flex;align-items:center;gap:14px;margin-bottom:12px;font-size:11.5px;color:var(--ink)}
.contact-row b{width:27px;height:27px;background:var(--green);display:flex;align-items:center;justify-content:center}
.news-input{width:229px;height:36px;border:1px solid #ddd;background:var(--white);font-size:11.5px;padding:0 14px;display:flex;align-items:center;color:#888}
.news-send{margin-top:8px;width:114px;height:36px;background:var(--green);color:var(--white);font-size:12px;font-weight:600;display:flex;align-items:center;justify-content:center}
.bottom-bar{position:absolute;left:0;top:2328px;width:1200px;height:34px;background:var(--green);color:var(--white);font-size:11.5px;padding-left:88px;line-height:34px}
.to-top{position:absolute;left:1068px;top:2302px;width:46px;height:46px;border-radius:50%;background:var(--white);box-shadow:0 1px 4px rgba(0,0,0,.2);display:flex;align-items:center;justify-content:center}
</style>
</head>
<body>

<header class="site-header">
  <div class="brand">
    <span class="brand-mark"></span>
    <div class="brand-name">Brinkhaven Painting and Home Services Experts<span>• Painting • Landscaping/Mowing • Window Washing • Maid Services</span></div>
  </div>
  <nav class="main-nav">
    <a class="active">Home</a><a>Who we are</a><a>What we do</a><a>Client experiences</a><a>Career Opportunities</a>
  </nav>
</header>

<section class="hero">
  <div class="hero-photo" role="img" aria-label="Smiling mother with two young children, hands covered in green paint, in a bright home"></div>
  <div class="hero-copy">
    <h1>Welcome</h1>
    <p>Lorem Ipsum is simply dummy text of the printing and type-setting industry. Lorem Ipsum has been the industry's standard dummy text ever since the 1500s</p>
  </div>
  <span class="btn">Read More</span>
  <span class="slide-arrow prev"><svg width="12" height="12" viewBox="0 0 12 12"><path d="M8 2 4 6l4 4" fill="none" stroke="#fff" stroke-width="2"/></svg></span>
  <span class="slide-arrow next"><svg width="12" height="12" viewBox="0 0 12 12"><path d="M4 2l4 4-4 4" fill="none" stroke="#fff" stroke-width="2"/></svg></span>
  <span class="slide-dot"></span>
</section>

<section class="who">
  <h2>Who We Are</h2>
  <p>Lorem Ipsum is simply dummy text of the printing and typesetting industry. Lorem Ipsum has been the industry's standard dummy text ever since the 1500s, when an unknown printer took a galley of type and scrambled it to make a type specimen book. It has survived not only five centuries, but also the leap into electronic typesetting, remaining essentially unchanged. It was popularised in the 1960s with the release of Letraset sheets containing Lorem Ipsum passages, and more recently with desktop publishing software like Aldus PageMaker including versions of Lorem Ipsum.</p>
  <span class="btn">Read More</span>
</section>

<svg class="collage" viewBox="0 0 430 340" role="img" aria-label="Diamond collage of family moments and houses with front yards">
  <defs>
    <linearGradient id="gFamily" x1="0" y1="0" x2="1" y2="1"><stop offset="0" stop-color="#d8c2b0"/><stop offset="1" stop-color="#8f7d74"/></linearGradient>
    <linearGradient id="gHouse" x1="0" y1="0" x2="0" y2="1"><stop offset="0" stop-color="#4d7fc4"/><stop offset="1" stop-color="#6c6a55"/></linearGradient>
    <linearGradient id="gSoft" x1="0" y1="0" x2="1" y2="1"><stop offset="0" stop-color="#f1e6dc"/><stop offset="1" stop-color="#c9b3a1"/></linearGradient>
  </defs>
  <g stroke="#fff" stroke-width="4">
    <polygon points="255,0 335,80 255,160 175,80" fill="url(#gFamily)"/>
    <polygon points="175,80 255,160 175,240 95,160" fill="url(#gHouse)"/>
    <polygon points="335,80 415,160 335,240 255,160" fill="url(#gSoft)"/>
    <polygon points="95,160 175,240 95,320 15,240" fill="#6e6a63"/>
    <polygon points="255,160 335,240 255,320 175,240" fill="#e6ddd6"/>
    <polygon points="175,240 215,280 175,320 135,280" fill="#d9d9d9"/>
  </g>
</svg>

<section class="services">
  <h2>What We Do</h2>
  <div class="service" style="left:67px">
    <svg width="120" height="130" viewBox="0 0 120 130"><polygon points="60,3 115,34 115,96 60,127 5,96 5,34" fill="none" stroke="#999" stroke-width="3"/><g fill="#8a8a8a"><rect x="50" y="44" width="24" height="14" rx="2" transform="rotate(-45 62 51)"/><rect x="42" y="58" width="8" height="28" rx="3" transform="rotate(-45 46 72)"/></g></svg>
    <h3>Service 1</h3>
    <p>Lorem Ipsum is simply dummy text of the printing and typesetting industry. Lorem Ipsum has been.</p>
    <span class="btn grey">Read More</span>
  </div>
  <div class="service" style="left:432px">
    <svg width="120" height="130" viewBox="0 0 120 130"><polygon points="60,3 115,34 115,96 60,127 5,96 5,34" fill="var(--green)"/><g fill="#fff"><rect x="40" y="40" width="34" height="14" rx="2"/><path d="M74 46h6v14H58v8" fill="none" stroke="#fff" stroke-width="3"/><rect x="54" y="68" width="8" height="22" rx="2"/></g></svg>
    <h3>Service 2</h3>
    <p>Lorem Ipsum is simply dummy text of the printing and typesetting industry. Lorem Ipsum has been.</p>
    <span class="btn">Read More</span>
  </div>
  <div class="service" style="left:793px">
    <svg width="120" height="130" viewBox="0 0 120 130"><polygon points="60,3 115,34 115,96 60,127 5,96 5,34" fill="none" stroke="#999" stroke-width="3"/><g fill="#8a8a8a"><rect x="40" y="66" width="40" height="22"/><circle cx="64" cy="46" r="8"/><path d="M38 58h18l8 6H38z"/></g></svg>
    <h3>Service 3</h3>
    <p>Lorem Ipsum is simply dummy text of the printing and typesetting industry. Lorem Ipsum has been.</p>
    <span class="btn grey">Read More</span>
  </div>
</section>

<section class="promise" role="img" aria-label="Green tinted band over a smiling family photo">
  <h2>Our promise to quality and client experience</h2>
  <p>Lorem Ipsum is simply dummy text of the printing and typesetting industry. Lorem Ipsum has been the industry's standard dummy text ever since the 1500s</p>
  <span class="btn light">Read More</span>
</section>

<section class="clients">
  <h2>Client Experiences</h2>
  <article class="testimonial" style="left:88px">
    <div class="t-frame"></div>
    <div class="t-photo" role="img" aria-label="Portrait of client in white shirt and tie"></div>
    <span class="t-quote">“</span>
    <h4 class="t-name">Daniel Harlow</h4>
    <p class="t-text">Lorem Ipsum is simply dummy text of the printing and typesetting industry. Lorem Ipsum has been the indus-try's standard dummy text ever since the 1500s</p>
    <div class="stars"><svg width="72" height="14" viewBox="0 0 72 14"><g fill="var(--star)"><path id="st" d="M7 0l2 5h5l-4 3 1.5 5L7 10l-4.5 3L4 8 0 5h5z"/><use href="#st" x="15"/><use href="#st" x="30"/><use href="#st" x="45"/></g><use href="#st" x="60" fill="var(--star-off)"/></svg></div>
  </article>
  <article class="testimonial" style="left:624px">
    <div class="t-frame"></div>
    <div class="t-photo" role="img" aria-label="Portrait of client in grey scarf and jacket"></div>
    <span class="t-quote">“</span>
    <h4 class="t-name">Peter Vance</h4>
    <p class="t-text">Lorem Ipsum is simply dummy text of the printing and typesetting industry. Lorem Ipsum has been the indus-try's standard dummy text ever since the 1500s</p>
    <div class="stars"><svg width="72" height="14" viewBox="0 0 72 14"><g fill="var(--star)"><use href="#st"/><use href="#st" x="15"/><use href="#st" x="30"/><use href="#st" x="45"/></g><use href="#st" x="60" fill="var(--star-off)"/></svg></div>
  </article>
</section>
<div class="pager"><i></i><i class="on"></i><i></i></div>

<section class="promos">
  <h2>Promotions</h2>
  <div class="promo" style="left:88px">
    <svg width="188" height="152" viewBox="0 0 188 152"><path d="M3 44 94 3l91 41" fill="none" stroke="#8c8c8c" stroke-width="7"/><rect x="16" y="42" width="7" height="110" fill="#8c8c8c"/><rect x="165" y="42" width="7" height="110" fill="#8c8c8c"/></svg>
    <h3>Promotion 1</h3><p>Lorem Ipsum is simply dummy text ever since the 1500s</p>
  </div>
  <div class="promo" style="left:356px">
    <svg width="188" height="152" viewBox="0 0 188 152"><path d="M3 44 94 3l91 41" fill="none" stroke="#8c8c8c" stroke-width="7"/><rect x="16" y="42" width="7" height="110" fill="#8c8c8c"/><rect x="165" y="42" width="7" height="110" fill="#8c8c8c"/></svg>
    <h3>Promotion 2</h3><p>Lorem Ipsum is simply dummy text ever since the 1500s</p>
  </div>
  <div class="promo" style="left:627px">
    <svg width="188" height="152" viewBox="0 0 188 152"><path d="M3 44 94 3l91 41" fill="none" stroke="#8c8c8c" stroke-width="7"/><rect x="16" y="42" width="7" height="110" fill="#8c8c8c"/><rect x="165" y="42" width="7" height="110" fill="#8c8c8c"/></svg>
    <h3>Promotion3</h3><p>Lorem Ipsum is simply dummy text ever since the 1500s</p>
  </div>
  <div class="promo" style="left:913px">
    <svg width="188" height="152" viewBox="0 0 188 152"><path d="M3 44 94 3l91 41" fill="none" stroke="#8c8c8c" stroke-width="7"/><rect x="16" y="42" width="7" height="110" fill="#8c8c8c"/><rect x="165" y="42" width="7" height="110" fill="#8c8c8c"/></svg>
    <h3>Promotion 4</h3><p>Lorem Ipsum is simply dummy text ever since the 1500s</p>
  </div>
</section>

<section class="careers">
  <div class="careers-photo" role="img" aria-label="Worker jumping happily in front of a house with a tiled roof"></div>
  <h2>Career opportunities<em>Join The team</em></h2>
  <p>Lorem Ipsum is simply dummy text of the printing and typesetting industry. Lorem Ipsum has been the industry's standard dummy text ever since the 1500s, when an unknown printer took a galley .</p>
  <span class="btn grey">Submit Resume</span>
</section>

<footer class="site-footer">
  <div class="f-col" style="left:88px;width:240px">
    <h4>About Us</h4>
    <p>Lorem Ipsum is simply dummy text of the printing and typesetting industry. Lorem Ipsum has been the industry's</p>
    <div class="social" aria-label="Social media links"><span></span><span></span><span></span><span></span></div>
  </div>
  <div class="f-col" style="left:397px">
    <h4>Useful Links</h4>
    <ul><li>Site Map</li><li>Email</li><li>Privacy Policy</li><li>Terms of Service</li><li>Delivery and Returns</li></ul>
  </div>
  <div class="f-col" style="left:598px">
    <h4>Get In Touch</h4>
    <div class="contact-row"><b><svg width="13" height="13" viewBox="0 0 24 24"><path d="M6.6 10.8a15 15 0 0 0 6.6 6.6l2.2-2.2c.3-.3.7-.4 1-.2 1.1.4 2.3.6 3.6.6.6 0 1 .4 1 1V20c0 .6-.4 1-1 1A17 17 0 0 1 3 4c0-.6.4-1 1-1h3.5c.6 0 1 .4 1 1 0 1.3.2 2.5.6 3.6.1.3 0 .7-.2 1z" fill="#fff"/></svg></b>123 -456-7890</div>
    <div class="contact-row"><b><svg width="13" height="10" viewBox="0 0 13 10"><rect x=".5" y=".5" width="12" height="9" fill="none" stroke="#fff"/><path d="M.5.5l6 5 6-5" fill="none" stroke="#fff"/></svg></b>info@brinkhavenhomecare.example</div>
  </div>
  <div class="f-col" style="left:871px">
    <h4>Newsletter</h4>
    <div class="news-input">Email</div>
    <div class="news-send">SEND</div>
  </div>
</footer>
<div class="bottom-bar">Copyright 2016 | All Right Reserved</div>
<span class="to-top"><svg width="12" height="8" viewBox="0 0 12 8"><path d="M1 7l5-5 5 5" fill="none" stroke="var(--green)" stroke-width="2"/></svg></span>

</body>
</html>
```